Digital Album Cover - Frosted Lanterns (Night Falls Still)

HiI need a digital album cover for a piano instrumental cover single

Artist: Corey Dalton
Title: Frosted Lanterns (Night Falls Still)

The song was originally by Derek Holloway

Please use my logo

You can listen to the track herehttps://soundcloud.com/coreydaltonkeys/frosted-lanterns-night-falls-still-piano-instrumental-cover

Requirements
Must have
• My logo design Corey Dalton

```html
<!DOCTYPE html>
<html lang="en">
<head>
<meta charset="utf-8">
<title>Frosted Lanterns (Night Falls Still) – Corey Dalton</title>
<link rel="stylesheet" href="https://fonts.googleapis.com/css2?family=Montserrat:wght@500;600;700&display=swap">
<style>
  :root {
    --ink-light: #ffffff;
    --keys-cream: #efe6b4;
    --keys-gold: #b9a870;
    --wood-brown: #5e4f33;
    --shadow-teal: #18252a;
    --haze: #8f9277;
  }
  html, body {
    margin: 0;
    padding: 0;
    width: 1186px;
    height: 1200px;
    overflow: hidden;
    background: var(--shadow-teal);
  }
  .cover {
    position: relative;
    width: 1186px;
    height: 1200px;
    overflow: hidden;
    font-family: "Montserrat", Arial, sans-serif;
    color: var(--ink-light);
  }
  .cover__photo {
    position: absolute;
    inset: 0;
    background:
      radial-gradient(ellipse 70% 45% at 78% 38%, var(--keys-cream) 0%, rgba(239,230,180,0.55) 45%, rgba(239,230,180,0) 75%),
      radial-gradient(ellipse 60% 40% at 20% 10%, rgba(214,204,150,0.8) 0%, rgba(214,204,150,0) 70%),
      radial-gradient(ellipse 70% 55% at 10% 85%, var(--shadow-teal) 0%, rgba(24,37,42,0) 75%),
      linear-gradient(160deg, var(--haze) 0%, var(--keys-gold) 40%, var(--wood-brown) 75%, #3a3426 100%);
  }
  .cover__ornament {
    position: absolute;
    left: 290px;
    top: 222px;
    width: 590px;
    height: 170px;
    border-radius: 50%;
    background: radial-gradient(ellipse at center, rgba(255,255,255,0.22) 0%, rgba(255,255,255,0) 70%);
  }
  .title {
    position: absolute;
    left: 0;
    right: 0;
    top: 430px;
    margin: 0;
    display: flex;
    flex-direction: column;
    align-items: center;
    text-transform: uppercase;
    line-height: 1;
    font-weight: 700;
  }
  .title__main {
    font-weight: 700;
    font-size: 112px;
    letter-spacing: 1px;
  }
  .title__main + .title__main {
    margin-top: 8px;
  }
  .title__sub {
    font-weight: 600;
    font-size: 54px;
    letter-spacing: 2px;
    margin-top: 26px;
  }
  .title__rule {
    width: 648px;
    height: 5px;
    background: var(--ink-light);
    margin-top: 32px;
  }
  .artist {
    position: absolute;
    left: 626px;
    top: 1012px;
    display: flex;
    align-items: center;
    gap: 24px;
  }
  .artist__dot {
    width: 106px;
    height: 106px;
    border-radius: 50%;
    background: var(--ink-light);
  }
  .artist__name {
    font-weight: 500;
    font-size: 40px;
    text-transform: uppercase;
  }
</style>
</head>
<body>
  <main class="cover">
    <div class="cover__photo" role="img" aria-label="Soft-focus close-up of piano keys in warm cream and gold light with faint snowflakes"></div>

    <div class="cover__ornament" role="img" aria-label="Star with two curved swoops above the title"></div>

    <h1 class="title">
      <span class="title__main">Frosted</span>
      <span class="title__main">Lanterns</span>
      <span class="title__sub">(Night Falls Still)</span>
      <span class="title__rule"></span>
    </h1>

    <div class="artist">
      <span class="artist__dot"></span>
      <span class="artist__name">CoreyDalton</span>
    </div>
  </main>
</body>
</html>
```